Banner Ad for Weight Loss Product Site

We need a banner ad design for a new company selling a weight loss online programme (Ebook). The product is called "Your FitRoute" and is suitable for people that want to lose weight fast and without doing sports, regardless of age. We would like to see designs that are eye-catching and at its best animated like in the example files. The final design should exhibit a professional look that encourages the customers to buy our product. The text should be "Persönlicher Diätplan zum Abnehmen?" as a title and "Jetzt informieren" for the button field. Thank you!

```html
<!DOCTYPE html>
<html lang="de">
<head>
<meta charset="utf-8">
<title>Your FitRoute – Banner</title>
<link rel="stylesheet" href="https://fonts.googleapis.com/css2?family=Open+Sans:wght@300;400;700&display=swap">
<style>
  :root {
    --page-bg: #ececec;
    --panel-top: #ffffff;
    --panel-bottom: #dcdcdc;
    --brand-green: #6aa51e;
    --brand-green-dark: #4f8a12;
    --accent-yellow: #f2c21b;
    --title-grey: #5a5a5a;
    --arrow-grey: #6b6b6b;
    --cta-orange: #f39419;
    --cta-orange-dark: #e06d0c;
    --white: #ffffff;
  }
  * { box-sizing: border-box; margin: 0; padding: 0; }
  html, body {
    width: 1200px;
    height: 721px;
    overflow: hidden;
    background: var(--page-bg);
    font-family: "Open Sans", Arial, sans-serif;
  }
  .banner {
    position: absolute;
    left: 296px;
    top: 14px;
    width: 607px;
    height: 530px;
    overflow: hidden;
    background: radial-gradient(ellipse at 45% 45%, var(--panel-top) 0%, #f3f3f3 45%, var(--panel-bottom) 100%);
  }
  .banner__shapes {
    position: absolute;
    inset: 0;
    width: 607px;
    height: 530px;
  }
  .banner__title {
    position: absolute;
    left: 26px;
    top: 66px;
    font-weight: 300;
    font-size: 46px;
    line-height: 56px;
    color: var(--title-grey);
    letter-spacing: -0.2px;
  }
  .banner__model {
    position: absolute;
    left: 412px;
    top: 22px;
    width: 190px;
    height: 420px;
    border-radius: 40px 40px 8px 8px;
    background: linear-gradient(180deg, #d9d3cc 0%, #cfc6bc 45%, #b9b2aa 75%, #8e8a86 100%);
    opacity: 0.85;
  }
  .banner__product {
    position: absolute;
    left: 222px;
    top: 255px;
    width: 180px;
    height: 172px;
    border-radius: 6px;
    background: linear-gradient(160deg, #f4f4ef 0%, #dfe6d3 55%, #a9c77c 100%);
    box-shadow: 0 2px 6px rgba(0,0,0,0.15);
  }
  .brand {
    position: absolute;
    left: 26px;
    top: 368px;
    width: 150px;
    height: 150px;
    border-radius: 50%;
    background: var(--brand-green-dark);
    display: flex;
    align-items: center;
    justify-content: center;
    text-align: center;
  }
  .brand__name {
    font-weight: 400;
    font-size: 26px;
    line-height: 30px;
    color: var(--white);
  }
  .cta {
    position: absolute;
    left: 226px;
    top: 456px;
    width: 330px;
    height: 50px;
    border-radius: 25px;
    background: linear-gradient(180deg, var(--cta-orange) 0%, var(--cta-orange-dark) 100%);
    box-shadow: 0 3px 6px rgba(0,0,0,0.25);
    display: flex;
    align-items: center;
    padding-left: 28px;
    color: var(--white);
    font-weight: 700;
    font-size: 23px;
    text-decoration: none;
  }
  .cta__icon {
    position: absolute;
    right: 12px;
    top: 8px;
    width: 34px;
    height: 34px;
    border-radius: 8px;
    background: var(--white);
  }
</style>
</head>
<body>
  <div class="banner">
    <svg class="banner__shapes" viewBox="0 0 607 530" aria-hidden="true">
      <path d="M0 0 H607 V20 C460 70 250 30 0 60 Z" fill="var(--brand-green)"/>
      <path d="M0 60 C250 30 460 70 607 20" fill="none" stroke="var(--accent-yellow)" stroke-width="6"/>
      <path d="M0 440 C200 420 420 440 607 425 V530 H0 Z" fill="var(--brand-green)"/>
      <path d="M0 440 C200 420 420 440 607 425" fill="none" stroke="var(--accent-yellow)" stroke-width="6"/>
      <path d="M76 272 C100 312 140 332 196 334" fill="none" stroke="var(--arrow-grey)" stroke-width="3" stroke-linecap="round"/>
      <path d="M182 322 L200 334 L182 346" fill="none" stroke="var(--arrow-grey)" stroke-width="3" stroke-linecap="round" stroke-linejoin="round"/>
    </svg>

    <h1 class="banner__title">Persönlicher<br>Diätplan zum<br>Abnehmen?</h1>

    <div class="banner__model" role="img" aria-label="Photo of a smiling fit woman in sportswear pointing forward with a measuring tape around her waist"></div>
    <div class="banner__product" role="img" aria-label="Product bundle: ebook cover, disc and opened plan pages"></div>

    <div class="brand"><span class="brand__name">Your<br>FitRoute</span></div>

    <a class="cta" href="#">Jetzt informieren
      <span class="cta__icon">
        <svg width="34" height="34" viewBox="0 0 34 34" aria-hidden="true">
          <path d="M14 10 L21 17 L14 24" fill="none" stroke="var(--cta-orange-dark)" stroke-width="3.5" stroke-linecap="round" stroke-linejoin="round"/>
        </svg>
      </span>
    </a>
  </div>
</body>
</html>
```